Dr. Marissa Tevlin Medical/Chiropractic Business Card

Dr. Tevlin is a chiropractor and will require a business card that she uses every single day to book appointments on the back side of the card. Currently the office name goes by Dr. Marissa Tevlin. The chiropractic profession is based on the diagnosis and manipulative treatment of misalignments of the joints, especially those of the spinal column, which are held to cause other disorders by affecting the nerves, muscles, and organs. Dr. Marissa Tevlin is looking for a contemporary and minimalistic design.

Industry/Entity Type

Medical

Contact Information for Business Card

Name: Dr. Marissa Tevlin; Address: 748 Harcastle Rd South, London, ON N5R 2K7; Phone Number: 519.274.6193; Fax: 519.281.5046; email: marissa.tevlin@quorvamail.com

Requirements
Must have
• ability to write multiple appointments date/time on the back of card

```html
<!DOCTYPE html>
<html lang="en">
<head>
<meta charset="utf-8">
<title>Dr. Marissa Tevlin – Business Card</title>
<link href="https://fonts.googleapis.com/css2?family=Lato:wght@400;700;900&display=swap" rel="stylesheet">
<style>
  :root {
    --blue: #0b57b0;
    --ink: #2b2b2b;
    --muted: #555;
    --line: #4f79b8;
    --paper: #f7f7f7;
    --stage: #2a2a2a;
  }
  * { box-sizing: border-box; margin: 0; padding: 0; }
  html, body { width: 1200px; height: 873px; overflow: hidden; }
  body {
    background: var(--stage);
    font-family: "Lato", sans-serif;
    position: relative;
  }
  .card {
    position: absolute;
    width: 540px;
    height: 310px;
    background: linear-gradient(160deg, #ffffff 0%, var(--paper) 60%, #ececec 100%);
    border-radius: 12px;
    overflow: hidden;
    box-shadow: 0 14px 30px rgba(0,0,0,.45);
  }
  .card--back { left: 50px; top: 281px; }
  .card--front { left: 610px; top: 281px; }

  /* Back: appointment card */
  .appt__header {
    position: absolute; left: 0; right: 0; top: 0; height: 32px;
    background: var(--blue);
    color: #fff; font-weight: 700; font-size: 16px;
    display: flex; align-items: center; justify-content: center;
  }
  .appt__footer {
    position: absolute; left: 0; right: 0; bottom: 0; height: 32px;
    background: var(--blue);
    color: #fff; font-size: 15px;
    display: flex; align-items: center; justify-content: center;
    letter-spacing: .2px;
  }
  .appt__field {
    position: absolute; left: 30px; right: 30px;
    border-bottom: 2px solid var(--line);
    font-weight: 700; color: var(--muted); font-size: 15px;
    padding-bottom: 2px; line-height: 18px;
  }
  .appt__field--name { top: 46px; }
  .appt__days {
    position: absolute; left: 30px; right: 30px; top: 88px;
    display: flex; justify-content: space-between;
  }
  .day {
    display: flex; align-items: center; gap: 5px;
    font-weight: 700; color: var(--muted); font-size: 13px;
  }
  .day__box {
    width: 17px; height: 17px; border: 2px solid var(--blue); border-radius: 4px;
  }
  .appt__slot { position: absolute; left: 30px; right: 30px; height: 22px; }
  .appt__slot--1 { top: 130px; }
  .appt__slot--2 { top: 172px; }
  .appt__slot--3 { top: 214px; }
  .appt__slot .appt__field { top: 0; }
  .appt__field--date { left: 0; right: auto; width: 200px; }
  .appt__field--time {
    left: 220px; right: 0; display: flex; justify-content: space-between;
  }

  /* Front: identity */
  .front__bands { position: absolute; inset: 0; }
  .front__identity {
    position: absolute; right: 310px; top: 112px; text-align: right;
  }
  .front__name { color: var(--blue); font-weight: 900; font-size: 20px; }
  .front__role { color: var(--ink); font-size: 14px; margin-top: 1px; }
  .front__address {
    margin-top: 26px; color: var(--blue); font-weight: 700; font-size: 15px; line-height: 1.2;
  }
  .front__divider {
    position: absolute; left: 248px; top: 100px; width: 2px; height: 120px;
    background: linear-gradient(var(--blue), rgba(11,87,176,0));
  }
  .front__contacts {
    position: absolute; left: 266px; top: 104px; list-style: none;
  }
  .contact {
    display: flex; align-items: center; gap: 10px;
    font-size: 13.5px; color: var(--ink); height: 30px;
  }
  .contact__icon {
    width: 22px; height: 22px; border-radius: 4px; background: var(--blue);
    display: flex; align-items: center; justify-content: center; flex: none;
  }
</style>
</head>
<body>

<section class="card card--back" aria-label="Appointment card, back side">
  <div class="appt__header">Appointment Card</div>
  <div class="appt__field appt__field--name">Name</div>
  <div class="appt__days">
    <span class="day">Mon <span class="day__box"></span></span>
    <span class="day">Tue <span class="day__box"></span></span>
    <span class="day">Wed <span class="day__box"></span></span>
    <span class="day">Thu <span class="day__box"></span></span>
    <span class="day">Fri <span class="day__box"></span></span>
    <span class="day">Sat <span class="day__box"></span></span>
    <span class="day">Sun <span class="day__box"></span></span>
  </div>
  <div class="appt__slot appt__slot--1">
    <div class="appt__field appt__field--date">Date:</div>
    <div class="appt__field appt__field--time"><span>Time:</span><span>AM</span><span>PM</span></div>
  </div>
  <div class="appt__slot appt__slot--2">
    <div class="appt__field appt__field--date">Date:</div>
    <div class="appt__field appt__field--time"><span>Time:</span><span>AM</span><span>PM</span></div>
  </div>
  <div class="appt__slot appt__slot--3">
    <div class="appt__field appt__field--date">Date:</div>
    <div class="appt__field appt__field--time"><span>Time:</span><span>AM</span><span>PM</span></div>
  </div>
  <div class="appt__footer">If you are unable to make your visit, then pl call us &amp; reschedule...</div>
</section>

<section class="card card--front" aria-label="Business card, front side">
  <svg class="front__bands" width="540" height="310" viewBox="0 0 540 310" aria-hidden="true">
    <polygon points="0,0 540,0 540,26 0,14" fill="var(--blue)"/>
    <rect x="0" y="282" width="540" height="28" fill="var(--blue)"/>
  </svg>

  <div class="front__identity">
    <div class="front__name">Dr. Marissa Tevlin</div>
    <div class="front__role">Chiropractor</div>
    <div class="front__address">748 Harcastle Rd South,<br>London, ON N5R 2K7</div>
  </div>

  <div class="front__divider"></div>

  <ul class="front__contacts">
    <li class="contact">
      <span class="contact__icon">
        <svg width="14" height="14" viewBox="0 0 24 24" aria-hidden="true"><path fill="#fff" d="M3 9c0-3 4-5 9-5s9 2 9 5v2h-5V9c-1-.6-2.5-1-4-1s-3 .4-4 1v2H3z"/><rect x="6" y="13" width="12" height="8" rx="1.5" fill="#fff"/></svg>
      </span>
      519.274.6193
    </li>
    <li class="contact">
      <span class="contact__icon">
        <svg width="14" height="14" viewBox="0 0 24 24" aria-hidden="true"><rect x="7" y="3" width="10" height="6" fill="#fff"/><rect x="3" y="10" width="18" height="8" rx="2" fill="#fff"/><rect x="7" y="15" width="10" height="6" fill="#fff" stroke="var(--blue)" stroke-width="1.5"/></svg>
      </span>
      519.281.5046
    </li>
    <li class="contact">
      <span class="contact__icon">
        <svg width="14" height="14" viewBox="0 0 24 24" aria-hidden="true"><g fill="none" stroke="#fff" stroke-width="2.6" stroke-linecap="round"><path d="M10 14l4-4"/><path d="M11 7l2-2a4 4 0 0 1 6 6l-2 2"/><path d="M13 17l-2 2a4 4 0 0 1-6-6l2-2"/></g></svg>
      </span>
      marissa.tevlin@quorvamail.com
    </li>
  </ul>
</section>

</body>
</html>
```